Business card for auto dealership

Looking for a clean modern design.
Would like attached logo incorporated

Industry/Entity Type

Car dealership

Contact Information for Business Card

Name, website, phone, cell, fax, email

```html
<!DOCTYPE html>
<html lang="en">
<head>
<meta charset="utf-8">
<title>Halvern Truck &amp; Auto Sales – Business Card</title>
<link href="https://fonts.googleapis.com/css2?family=Montserrat:wght@400;600&family=Roboto+Condensed:wght@400&display=swap" rel="stylesheet">
<style>
  :root {
    --backdrop: #dcdcdc;
    --card: #ffffff;
    --ink: #1b1b1f;
    --navy: #1e2030;
    --grey-band: #b4b4b8;
    --grey-soft: #e6e6e8;
    --grey-dot: #e2e2e2;
  }
  * { margin: 0; padding: 0; box-sizing: border-box; }
  html, body {
    width: 1200px; height: 1200px; overflow: hidden;
    background: var(--backdrop);
  }
  .card {
    position: absolute; left: 151px; width: 897px; height: 524px;
    background: var(--card); overflow: hidden;
  }
  .card--front { top: 59px; }
  .card--back { top: 610px; }

  .wordmark {
    position: absolute; color: var(--ink);
    font-family: "Montserrat", sans-serif; font-weight: 600;
    line-height: 1; letter-spacing: -0.01em;
  }
  .wordmark__name { display: block; }
  .wordmark__tag { display: block; letter-spacing: 0.04em; text-transform: uppercase; }

  .card--front .wordmark { left: 59px; top: 78px; }
  .card--front .wordmark__name { font-size: 84px; }
  .card--front .wordmark__tag { font-size: 17px; margin: 4px 0 0 96px; }

  .card--back .wordmark { left: 0; right: 0; top: 268px; text-align: center; }
  .card--back .wordmark__name { font-size: 124px; }
  .card--back .wordmark__tag { font-size: 26px; margin-top: 10px; padding-left: 60px; }

  .front-rule {
    position: absolute; left: 59px; top: 246px; width: 346px; height: 2px;
    background: var(--ink);
  }
  .person-name {
    position: absolute; left: 58px; top: 286px;
    font-family: "Roboto Condensed", sans-serif; font-weight: 400;
    font-size: 57px; color: var(--ink); line-height: 1;
  }
  .contact-list {
    position: absolute; list-style: none;
    font-family: "Montserrat", sans-serif; font-weight: 400;
    font-size: 22px; color: #2a2a2a;
  }
  .contact-list li { display: flex; align-items: center; height: 34.5px; }
  .contact-list svg { width: 15px; height: 15px; margin-right: 14px; fill: var(--ink); flex: none; }
  .contact-list--phones { left: 66px; top: 373px; }
  .contact-list--online { left: 513px; top: 408px; }

  .decor { position: absolute; left: 0; top: 0; }

  .ornament-band {
    position: absolute; left: 0; top: 24px; width: 897px; height: 132px;
    background: linear-gradient(180deg, var(--card) 0%, var(--grey-soft) 30%, var(--grey-band) 55%, var(--grey-soft) 80%, var(--card) 100%);
  }
</style>
</head>
<body>

<section class="card card--front">
  <svg class="decor" width="897" height="200" viewBox="0 0 897 200" aria-hidden="true">
    <polygon points="531,164 731,164 630,33" fill="var(--grey-dot)"/>
    <polygon points="732,0 897,0 814,81" fill="var(--navy)"/>
    <g fill="var(--navy)">
      <polygon points="689,151 699,151 721,116 711,116"/>
      <polygon points="717,151 727,151 749,116 739,116"/>
      <polygon points="745,151 755,151 777,116 767,116"/>
      <polygon points="773,151 783,151 805,116 795,116"/>
      <polygon points="801,151 811,151 833,116 823,116"/>
      <polygon points="829,151 839,151 861,116 851,116"/>
    </g>
  </svg>

  <div class="wordmark">
    <span class="wordmark__name">Halvern</span>
    <span class="wordmark__tag">Truck &amp; Auto Sales</span>
  </div>

  <div class="front-rule"></div>
  <h1 class="person-name">Marcus Delane</h1>

  <ul class="contact-list contact-list--phones">
    <li>
      <svg viewBox="0 0 16 16" aria-hidden="true"><path d="M4 0h8a1 1 0 0 1 1 1v14a1 1 0 0 1-1 1H4a1 1 0 0 1-1-1V1a1 1 0 0 1 1-1zm1 2v11h6V2z"/></svg>
      555-310-0100
    </li>
    <li>
      <svg viewBox="0 0 16 16" aria-hidden="true"><path d="M3.6 1 6 4.2 4.6 6c.9 2 2.5 3.6 4.5 4.5L11 9l3.2 2.4-1.4 2.9C7 14 2 9 1.8 3.2z"/></svg>
      555-310-0142
    </li>
    <li>
      <svg viewBox="0 0 16 16" aria-hidden="true"><path d="M4 1h7v4H4zM1 6h14v8H1zm3 2v2h2V8zm4 0v2h5V8zM4 11v1h9v-1z"/></svg>
      555-310-0199
    </li>
  </ul>

  <ul class="contact-list contact-list--online">
    <li>
      <svg viewBox="0 0 16 16" aria-hidden="true"><path d="M1 3h14v10H1zm1.5 1.2L8 8.5l5.5-4.3z"/></svg>
      office@halvernsales.com
    </li>
    <li>
      <svg viewBox="0 0 16 16" aria-hidden="true"><circle cx="8" cy="8" r="7"/><path d="M1 8h14M8 1c-3 3-3 11 0 14M8 1c3 3 3 11 0 14" stroke="#fff" stroke-width="1.2" fill="none"/></svg>
      www.halvernsales.com
    </li>
  </ul>
</section>

<section class="card card--back">
  <div class="ornament-band" role="img" aria-label="Decorative band of grey and navy geometric shapes across the top of the card"></div>

  <div class="wordmark">
    <span class="wordmark__name">Halvern</span>
    <span class="wordmark__tag">Truck &amp; Auto Sales</span>
  </div>
</section>

</body>
</html>
```